The billboard should communicate confidence, energy and approachability while maintaining a professional, premium feel. Rather than relying on a standard agent photograph, property collage or crowded list of services, we would like an original creative idea that makes people look twice. This could involve a fun visual, clever headline, striking colour contrast or an unexpected real estate theme. The concept should feel positive and contemporary, with enough personality to become recognisable throughout the local community.

The key message should appeal to homeowners who are thinking about selling, preparing to sell or simply curious about the value of their property. Copy must be short, clear and conversational, supported by a direct call to action. The agent’s name, phone number and company branding should remain highly visible without competing with the main idea.

The finished billboard will measure 8.0 metres wide by 2.08 metres high (1224px x 324px), so the composition must suit a long landscape format. All important text and imagery should remain comfortably within safe margins and be legible from a distance. The design should avoid small writing, unnecessary detail and visual clutter.

The goal is to create a billboard that feels different from every other real estate sign in the area—something engaging, confident and easy to remember. It should build strong brand awareness, generate conversations and encourage local property owners to contact the agent when they are ready to make their next move. The concept should be adaptable for future campaigns, helping establish a consistent, distinctive and trusted local brand presence.

Target Market(s)

ages 30+

Industry/Entity Type

Real Estate

Requirements
Must have
• call Wade and phone number 0417 63 28 05
Nice to have
• Nice bright and yellow.. Exciting and grabbing

```html
<!DOCTYPE html>
<html lang="en">
<head>
<meta charset="utf-8">
<title>What's Your Home Worth – Lorne Bexley</title>
<link rel="stylesheet" href="https://fonts.googleapis.com/css2?family=Anton&family=Kalam:wght@700&family=Poppins:wght@700&display=swap">
<style>
  :root {
    --brand-yellow: #ffe512;
    --ink: #333333;
    --ink-soft: #555555;
    --paper: #ffffff;
    --visual-dark: #1a1a1a;
    --visual-gold: #f2c200;
  }
  html, body {
    margin: 0;
    padding: 0;
    width: 1200px;
    height: 312px;
    overflow: hidden;
    background: var(--paper);
  }
  .billboard {
    position: relative;
    width: 1200px;
    height: 312px;
    overflow: hidden;
    background: var(--paper);
  }
  .backdrop {
    position: absolute;
    inset: 0;
  }
  .headline {
    position: absolute;
    left: 30px;
    top: 26px;
    margin: 0;
    font-family: "Anton", sans-serif;
    font-weight: 400;
    font-size: 102px;
    line-height: 92px;
    letter-spacing: 1px;
    color: var(--ink);
    text-transform: uppercase;
    white-space: nowrap;
  }
  .headline span { display: block; }
  .tagline {
    position: absolute;
    left: 96px;
    top: 226px;
    margin: 0;
    line-height: 56px;
    color: var(--ink);
    white-space: nowrap;
  }
  .tagline .script {
    font-family: "Kalam", cursive;
    font-weight: 700;
    font-size: 44px;
  }
  .tagline .plain {
    font-family: "Poppins", sans-serif;
    font-weight: 700;
    font-size: 31px;
  }
  .hero-visual {
    position: absolute;
    left: 585px;
    top: 8px;
    width: 270px;
    height: 288px;
    border-radius: 40px;
    background: radial-gradient(circle at 50% 45%, var(--visual-dark) 0%, var(--visual-dark) 48%, var(--visual-gold) 100%);
  }
  .contact {
    position: absolute;
    left: 880px;
    top: 112px;
    font-family: "Anton", sans-serif;
    color: var(--ink);
    text-transform: uppercase;
  }
  .contact-call {
    margin: 0;
    font-size: 31px;
    line-height: 1.1;
    letter-spacing: 0.5px;
  }
  .contact-phone {
    margin: 2px 0 0;
    font-size: 50px;
    line-height: 1.1;
    letter-spacing: 0.5px;
    white-space: nowrap;
  }
  .brand-name {
    position: absolute;
    left: 878px;
    top: 228px;
    margin: 0;
    font-family: "Poppins", sans-serif;
    font-weight: 700;
    font-size: 40px;
    line-height: 1.3;
    color: var(--ink-soft);
    white-space: nowrap;
  }
</style>
</head>
<body>
  <main class="billboard">
    <svg class="backdrop" width="1200" height="312" viewBox="0 0 1200 312" aria-hidden="true">
      <polygon points="0,0 792,0 648,312 0,312" fill="var(--brand-yellow)"/>
      <polygon points="853,217 1200,217 1200,294 825,294" fill="var(--brand-yellow)"/>
    </svg>

    <h1 class="headline">
      <span>What’s your</span>
      <span>home worth</span>
    </h1>

    <p class="tagline"><span class="script">Curious?</span> <span class="plain">Let’s find out.</span></p>

    <div class="hero-visual" role="img" aria-label="Large glossy 3D black dollar sign and question mark with yellow edges"></div>

    <div class="contact">
      <p class="contact-call">Talk to Wade</p>
      <p class="contact-phone">0417 63 28 05</p>
    </div>

    <p class="brand-name">Lorne Bexley</p>
  </main>
</body>
</html>
```